Varro's Electrical & Solar Corflute Signage Design

So my plan is to put this design onto a 600 by 400 corflute sign (this sign will be printed out and cable tied to a fence FYI). I would like to have the name and the icon stand out. I need Varro's Electrical & Solar to be big and clear and I would like to have my "S" icon faded behind "Varro's Electrical & Solar" in the background.

I want to have my Lic No. - Top left with my ABN directly underneath. (I Want two ticks infront of them like this)
✓ Lic No. 582164K
✓ ABN 41 276 519 683

I want to have written on it: ALL ASPECTS OF ELECTRICAL (please use cool fonts and nothing too plain)
I also want to have: YOUR LOCAL TRUSTED ELECTRICIAN but if it looks too dicky then just have "all aspects of electrical" and just "free quotes • fast service" somewhere.
Directly underneath (smaller but still clear): FREE QUOTES • FAST SERVICE

At the bottom, I need my phone number big and clear - 0438 617 905 I would like this on a banner meaning like a cool strip at the bottom. (Please make the strip/banner look cool and not boring. Maybe shade the colour or something)
I also want the Facebook & Instagram icons on there so people can look us up on facebook & Instagram (make them match the colour of my logo or you could try any other colour that works)
Thank you so much!!

Colors

Designer to choose colors to be used in the design.

Requirements
Should not have
• no different colours other then the colours on my logo and icon

```html
<!DOCTYPE html>
<html lang="en">
<head>
<meta charset="utf-8">
<title>Varro's Electrical &amp; Solar – Corflute Sign</title>
<link rel="stylesheet" href="https://fonts.googleapis.com/css2?family=Exo+2:ital,wght@1,900&family=Montserrat:wght@500;600;700;800&display=swap">
<style>
  :root {
    --backdrop: #e4e4e4;
    --sign-black: #050505;
    --white: #ffffff;
    --green-dark: #1f9a3c;
    --green-mid: #3dbb4f;
    --green-light: #7ad47c;
    --shadow-grey: #555a5c;
    --faint: rgba(255, 255, 255, 0.07);
    --ink: #0b0b0b;
  }
  * { margin: 0; padding: 0; box-sizing: border-box; }
  html, body {
    width: 1200px;
    height: 1200px;
    overflow: hidden;
    background: var(--backdrop);
  }
  .sign {
    position: absolute;
    left: 60px;
    top: 240px;
    width: 1080px;
    height: 720px;
    background: var(--sign-black);
    font-family: "Montserrat", sans-serif;
    color: var(--white);
    text-align: center;
    overflow: hidden;
  }
  .credentials {
    position: absolute;
    top: 34px;
    left: 34px;
    list-style: none;
    text-align: left;
    font-size: 20px;
    font-weight: 600;
    line-height: 1.6;
  }
  .credentials li { display: flex; align-items: center; gap: 10px; }
  .credentials svg { width: 20px; height: 20px; flex: none; }
  .brand-mark-bg {
    position: absolute;
    top: -20px;
    left: 415px;
    width: 250px;
    height: 250px;
    border-radius: 50%;
    background: var(--faint);
  }
  .brand-name {
    position: absolute;
    top: 38px;
    left: 0;
    width: 100%;
    font-weight: 800;
    color: var(--green-mid);
    line-height: 1;
  }
  .brand-name .brand-main {
    display: block;
    font-size: 96px;
    letter-spacing: 2px;
  }
  .brand-name .brand-sub {
    display: block;
    margin-top: 10px;
    font-size: 24px;
    letter-spacing: 6px;
  }
  .headline-lead {
    position: absolute;
    top: 222px;
    left: 0;
    width: 100%;
    font-size: 44px;
    font-weight: 500;
    letter-spacing: 0.5px;
  }
  .headline-main {
    position: absolute;
    top: 262px;
    left: 0;
    width: 100%;
    font-family: "Exo 2", sans-serif;
    font-style: italic;
    font-weight: 900;
    font-size: 104px;
    line-height: 1.1;
    letter-spacing: 1px;
    background: linear-gradient(90deg, var(--green-dark), var(--green-light) 55%, var(--green-mid));
    -webkit-background-clip: text;
    background-clip: text;
    color: transparent;
    filter: drop-shadow(-5px 6px 0 var(--shadow-grey));
  }
  .tagline {
    position: absolute;
    top: 406px;
    left: 0;
    width: 100%;
    font-size: 24px;
    font-weight: 500;
    letter-spacing: 0.5px;
  }
  .offer {
    position: absolute;
    top: 452px;
    left: 0;
    width: 100%;
    font-size: 26px;
    font-weight: 800;
    color: var(--green-mid);
    letter-spacing: 0.5px;
  }
  .contact-band {
    position: absolute;
    top: 530px;
    left: 0;
    width: 100%;
    height: 160px;
    background: linear-gradient(90deg, var(--green-dark), var(--green-light) 50%, var(--green-dark));
    border-top: 6px solid var(--green-dark);
    border-bottom: 6px solid var(--green-dark);
    display: flex;
    align-items: center;
    justify-content: space-between;
    padding: 0 50px;
    color: var(--ink);
  }
  .phone {
    display: flex;
    align-items: center;
    gap: 18px;
    font-size: 76px;
    font-weight: 800;
    letter-spacing: 2px;
    line-height: 1;
  }
  .phone svg { width: 56px; height: 56px; flex: none; }
  .socials {
    display: flex;
    flex-direction: column;
    align-items: center;
    gap: 10px;
  }
  .social-dots { display: flex; gap: 14px; }
  .social-dots span {
    width: 44px;
    height: 44px;
    border-radius: 50%;
    background: var(--ink);
  }
  .social-handle {
    font-size: 19px;
    font-weight: 700;
  }
</style>
</head>
<body>
  <main class="sign">
    <ul class="credentials">
      <li><svg viewBox="0 0 20 20" aria-hidden="true"><path d="M3 10.5l4.5 4.5L17 5" fill="none" stroke="#3dbb4f" stroke-width="3" stroke-linecap="round" stroke-linejoin="round"/></svg>Lic No. 582164K</li>
      <li><svg viewBox="0 0 20 20" aria-hidden="true"><path d="M3 10.5l4.5 4.5L17 5" fill="none" stroke="#3dbb4f" stroke-width="3" stroke-linecap="round" stroke-linejoin="round"/></svg>ABN 41 276 519 683</li>
    </ul>

    <div class="brand-mark-bg" aria-hidden="true"></div>
    <h1 class="brand-name">
      <span class="brand-main">VARRO'S</span>
      <span class="brand-sub">ELECTRICAL &amp; SOLAR</span>
    </h1>

    <p class="headline-lead">ALL ASPECTS OF</p>
    <h2 class="headline-main">ELECTRICAL</h2>
    <p class="tagline">YOUR LOCAL TRUSTED ELECTRICIAN</p>
    <p class="offer">FREE QUOTES • FAST SERVICE</p>

    <div class="contact-band">
      <p class="phone">
        <svg viewBox="0 0 24 24" aria-hidden="true"><path fill="#0b0b0b" d="M6.6 10.8a15.1 15.1 0 0 0 6.6 6.6l2.2-2.2a1 1 0 0 1 1-.25 11.4 11.4 0 0 0 3.6.57 1 1 0 0 1 1 1V20a1 1 0 0 1-1 1A17 17 0 0 1 3 4a1 1 0 0 1 1-1h3.5a1 1 0 0 1 1 1c0 1.25.2 2.45.57 3.57a1 1 0 0 1-.25 1z"/></svg>
        0438 617 905
      </p>
      <div class="socials">
        <div class="social-dots" aria-hidden="true"><span></span><span></span></div>
        <p class="social-handle">@varroselectrical</p>
      </div>
    </div>
  </main>
</body>
</html>
```